Harbor Nightclub

Nightclub flyer., digital single sided, for KV and PX. I included samples of some previous flyers we've used. Sample Info:
HARBOR
FRIDAYS
FRI MAY 1 2020
DJ VORTAN (club floor)
DJ RUZO & DJ TAV (residents on the lounge floor)
4217 Marlow Avenue Sacramento
www.harborvenuehall.example for list/VIP inquiries

Target Market(s)

Upscale top 40 crowd but want some cool and artsy like the examples included.

Font styles to use
Sans Serif

Requirements
Must have
• Harbor Logo
Nice to have
• Would be nice if the flyer can be incorporated later with DJ photos (sometimes we will add dj photos to pixagram etc). Would like a big city type of feel.
Should not have
• Nothing too sexual.

```html
<!DOCTYPE html>
<html lang="en">
<head>
<meta charset="utf-8">
<title>Harbor Fridays – Flyer</title>
<link rel="stylesheet" href="https://fonts.googleapis.com/css2?family=Bodoni+Moda:wght@400;500&family=Barlow+Condensed:wght@700&family=Barlow:wght@700&display=swap">
<style>
  :root {
    --bg-deep: #140c0a;
    --glow-hot: #f4a03a;
    --glow-ember: #b4421a;
    --glow-dark: #3a1a10;
    --star-ink: #100b0a;
    --crowd-shade: #2a2522;
    --text-light: #ffffff;
    --badge-ink: #1a1210;
    --badge-paper: #ffffff;
  }
  html, body {
    margin: 0;
    padding: 0;
    overflow: hidden;
    background: var(--bg-deep);
  }
  .flyer {
    position: relative;
    width: 835px;
    height: 1200px;
    overflow: hidden;
    background: var(--bg-deep);
  }
  .stage-light {
    position: absolute;
    left: 0; top: 0;
    width: 835px; height: 1200px;
    background:
      radial-gradient(ellipse 60% 45% at 50% 50%, rgba(244,160,58,0.5), rgba(180,66,26,0.3) 45%, rgba(58,26,16,0.15) 75%, transparent 100%),
      linear-gradient(180deg, var(--glow-dark) 0%, var(--glow-ember) 48%, var(--glow-hot) 70%, var(--glow-dark) 86%, var(--bg-deep) 100%);
    opacity: 0.9;
  }
  .stars {
    position: absolute;
    left: 0; top: 0;
    width: 835px; height: 1200px;
  }
  .crowd {
    position: absolute;
    left: 0; top: 745px;
    width: 835px; height: 330px;
    background: linear-gradient(180deg, rgba(42,37,34,0) 0%, rgba(42,37,34,0.85) 30%, var(--crowd-shade) 65%, var(--bg-deep) 100%);
  }
  .venue-badge {
    position: absolute;
    left: 355px; top: 0;
    width: 124px; height: 102px;
    background: var(--badge-paper);
    display: flex;
    align-items: center;
    justify-content: center;
  }
  .venue-badge .name {
    font-family: "Bodoni Moda", serif;
    font-weight: 500;
    font-size: 21px;
    letter-spacing: 1px;
    color: var(--badge-ink);
  }
  .title {
    position: absolute;
    left: 0; top: 118px;
    width: 835px;
    margin: 0;
    text-align: center;
    font-family: "Bodoni Moda", serif;
    font-weight: 400;
    font-size: 88px;
    line-height: 122px;
    letter-spacing: 5px;
    color: var(--text-light);
  }
  .date {
    position: absolute;
    left: 540px; top: 408px;
    width: 275px;
    text-align: center;
    font-family: "Barlow Condensed", sans-serif;
    font-weight: 700;
    font-size: 70px;
    line-height: 86px;
    color: var(--text-light);
  }
  .headliner {
    position: absolute;
    left: 0; top: 636px;
    width: 826px;
    text-align: center;
    font-family: "Bodoni Moda", serif;
    font-weight: 500;
    font-size: 58px;
    letter-spacing: 1px;
    color: var(--text-light);
  }
  .resident {
    position: absolute;
    font-family: "Barlow Condensed", sans-serif;
    font-weight: 700;
    font-size: 72px;
    color: var(--text-light);
    -webkit-text-stroke: 2px #000;
    paint-order: stroke fill;
    white-space: nowrap;
  }
  .resident--left { left: 50px; top: 826px; transform: rotate(-8deg); }
  .resident--right { left: 500px; top: 812px; transform: rotate(-10deg); }
  .info {
    position: absolute;
    left: 0;
    width: 835px;
    margin: 0;
    text-align: center;
    font-family: "Barlow", sans-serif;
    font-weight: 700;
    font-size: 19px;
    color: var(--text-light);
  }
  .info--address { top: 1075px; }
  .info--web { top: 1134px; font-size: 20px; }
</style>
</head>
<body>
<main class="flyer">
  <div class="stage-light" role="img" aria-label="Glowing orange stage curtain of light streaks and sparkles"></div>

  <svg class="stars" viewBox="0 0 835 1200" aria-hidden="true">
    <defs>
      <polygon id="star-shape" points="0,-1 0.235,-0.324 0.951,-0.309 0.380,0.124 0.588,0.809 0,0.4 -0.588,0.809 -0.380,0.124 -0.951,-0.309 -0.235,-0.324"/>
    </defs>
    <g fill="var(--star-ink)">
      <use href="#star-shape" transform="translate(600 300) rotate(12) scale(230)" opacity="0.8"/>
      <use href="#star-shape" transform="translate(120 520) rotate(-10) scale(240)" opacity="0.85"/>
      <use href="#star-shape" transform="translate(380 470) rotate(-6) scale(340)" opacity="0.9"/>
      <use href="#star-shape" transform="translate(700 640) rotate(18) scale(260)" opacity="0.88"/>
      <use href="#star-shape" transform="translate(170 870) rotate(8) scale(150)" opacity="0.9"/>
      <use href="#star-shape" transform="translate(600 880) rotate(-14) scale(170)" opacity="0.9"/>
    </g>
  </svg>

  <div class="crowd" role="img" aria-label="Silhouetted crowd of people dancing with raised arms"></div>

  <div class="venue-badge">
    <span class="name">HARBOR</span>
  </div>

  <h1 class="title">HARBOR<br>FRIDAYS</h1>

  <div class="date">MAY 1ST<br>2020</div>

  <div class="headliner">DJ VORTAN</div>

  <div class="resident resident--left">DJ RUZO</div>
  <div class="resident resident--right">DJ TAV</div>

  <p class="info info--address">4217 Marlow Avenue Sacramento</p>
  <p class="info info--web">www.harborvenuehall.example for list/VIP inquiries</p>
</main>
</body>
</html>
```